App Design - Job Lantern Quokka

We require an App Design for our new App called 'Lantern Quokka'. This app is essentially an assistant to help Users prepare for job interviews, to help them get hired. <br/><br/>Users who download the App can view common Questions and Answers, save their favourite responses and also view common Interview Tips. <br/><br/>The vision for our App is for Users who are preparing for an interview (1 week before, 1 day before, even 1 hour before), are able to download, view and educate themselves on common questions and responses, and then be confident to land the job. <br/><br/>Our team has developed wireframes to help highlight what each screen should do and include. Please see attached document, which also highlights key requirements for the experience. Feel free to add/remove/edit what you see on these wireframes. Our preference is that you use Adobe XD please.<br/><br/>In terms of design guidelines, we want the experience to be simple, intuitive and 'memorable' to help Users to remember the questions/responses when they are in the interview. <br/><br/>The final design should communicate 'neat and clean professionalism'; we like the design of: marlo vane com au<br/><br/>Thank you for reading! Good luck !

Target Market(s)

Professional job seekers

Font styles to use
Sans Serif

Colors

Designer to choose colors to be used in the design.

Requirements
Must have
• Please see my PlanHive_UX file that I have uploaded
Nice to have
• Could you also please include some ideas on how we can incorporate Advertising into the app screens

```html
<!DOCTYPE html>
<html lang="en">
<head>
<meta charset="utf-8">
<title>Lantern Quokka – Home</title>
<link href="https://fonts.googleapis.com/css2?family=Nunito:wght@400;600;800;900&display=swap" rel="stylesheet">
<style>
  :root {
    --page-bg: #f4f5f7;
    --brand-blue: #1a55d6;
    --brand-blue-deep: #1645b8;
    --screen-bg: #e6e6e7;
    --card-bg: #f0f0f0;
    --ink: #1b1b1f;
    --icon-blue: #1f4fc4;
    --white: #ffffff;
  }
  * { box-sizing: border-box; margin: 0; padding: 0; }
  html, body {
    width: 1200px; height: 800px; overflow: hidden;
    background: var(--page-bg);
    font-family: "Nunito", sans-serif;
  }
  .canvas {
    width: 1200px; height: 800px;
    display: flex; justify-content: center; align-items: center;
  }
  .app-screen {
    position: relative;
    width: 375px; height: 800px;
    background: linear-gradient(180deg, #ececed 0%, var(--screen-bg) 100%);
    overflow: hidden;
  }
  .hero {
    position: absolute; top: 0; left: 0; right: 0; height: 252px;
    background: linear-gradient(160deg, #1d5be0 0%, var(--brand-blue) 55%, var(--brand-blue-deep) 100%);
  }
  .status-bar {
    position: absolute; top: 12px; left: 34px; right: 26px;
    display: flex; justify-content: space-between; align-items: center;
    color: var(--white); font-size: 10px; font-weight: 600;
  }
  .status-icons { display: flex; gap: 4px; align-items: center; }
  .hero-watermark {
    position: absolute; top: 52px; left: -6px; right: -6px;
    font-size: 58px; font-weight: 900; line-height: 0.95;
    color: rgba(255,255,255,0.08); text-align: center; letter-spacing: 1px;
    white-space: nowrap;
  }
  .app-title {
    position: absolute; top: 74px; left: 0; right: 0;
    text-align: center; color: var(--white);
    font-size: 19px; font-weight: 800; letter-spacing: 0.2px;
  }
  .menu { position: absolute; left: 14px; right: 14px; top: 0; }
  .menu-card {
    position: absolute; left: 0; width: 347px; height: 138px;
    background: var(--card-bg);
    border-radius: 4px;
    box-shadow: 0 2px 6px rgba(0,0,0,0.08);
    display: flex; flex-direction: column; align-items: center;
  }
  .menu-card--questions { top: 198px; }
  .menu-card--portfolio { top: 376px; }
  .menu-card--tips { top: 558px; }
  .menu-icon { margin-top: 22px; width: 60px; height: 60px; }
  .menu-label {
    margin-top: 14px; font-size: 16.5px; font-weight: 400; color: var(--ink);
  }
  .tips-figure {
    width: 60px; height: 60px; border-radius: 8px;
    background: linear-gradient(180deg, #d3dcf3, #bccbef);
  }
</style>
</head>
<body>
<div class="canvas">
  <main class="app-screen">
    <header class="hero" role="img" aria-label="Blue-tinted photo of hands writing notes at a desk">
      <div class="status-bar">
        <span class="status-time">9:41</span>
        <span class="status-icons">
          <svg width="12" height="8" viewBox="0 0 12 8"><rect x="0" y="6" width="2" height="2" fill="#fff"/><rect x="3" y="4" width="2" height="4" fill="#fff"/><rect x="6" y="2" width="2" height="6" fill="#fff"/><rect x="9" y="0" width="2" height="8" fill="#fff"/></svg>
          <svg width="11" height="8" viewBox="0 0 11 8"><path d="M5.5 8 L3.5 5.6 A3 3 0 0 1 7.5 5.6 Z M1.6 3.8 A5.6 5.6 0 0 1 9.4 3.8 L8.5 4.8 A4.3 4.3 0 0 0 2.5 4.8 Z" fill="#fff"/></svg>
          <svg width="16" height="8" viewBox="0 0 16 8"><rect x="0.5" y="0.5" width="13" height="7" rx="1.5" fill="none" stroke="#fff"/><rect x="2" y="2" width="10" height="4" fill="#fff"/><rect x="14.2" y="2.5" width="1.2" height="3" fill="#fff"/></svg>
        </span>
      </div>
      <div class="hero-watermark" aria-hidden="true">LANTERN<br>QUOKKA</div>
      <h1 class="app-title">LANTERN QUOKKA</h1>
    </header>

    <nav class="menu">
      <a class="menu-card menu-card--questions">
        <svg class="menu-icon" viewBox="0 0 60 60" fill="none" stroke="var(--icon-blue)" stroke-width="2.6" stroke-linejoin="round">
          <path d="M24 4 A20 20 0 1 1 14 41 L5 44 L8 35 A20 20 0 0 1 24 4 Z"/>
          <path d="M37 24 A15 15 0 1 1 42 55 L55 57 L52 49 A15 15 0 0 0 37 24"/>
          <path d="M19 17 A5 5 0 1 1 25 22 Q24 23 24 27" stroke-linecap="round"/>
          <circle cx="24" cy="32" r="1" fill="var(--icon-blue)"/>
        </svg>
        <span class="menu-label">View Questions &amp; Responses</span>
      </a>

      <a class="menu-card menu-card--portfolio">
        <svg class="menu-icon" viewBox="0 0 60 60" fill="none" stroke="var(--icon-blue)" stroke-width="2.4" stroke-linejoin="round" stroke-linecap="round">
          <path d="M8 4 H44 V22 M44 44 V56 H8 Z"/>
          <circle cx="24" cy="17" r="7"/>
          <path d="M13 30 H36 M13 36 H34 M13 42 H32 M13 48 H28"/>
          <path d="M40 50 L38 56 L43 52 L55 30 L52 28 Z"/>
        </svg>
        <span class="menu-label">My Question Portfolio</span>
      </a>

      <a class="menu-card menu-card--tips">
        <div class="menu-icon tips-figure" role="img" aria-label="Icon of two people talking across a table"></div>
        <span class="menu-label">Interview Tips</span>
      </a>
    </nav>
  </main>
</div>
</body>
</html>
```